Dutch craft distillery needs labels designed for Gin bottle

We are a small craft distillery based in The Netherlands. We are currently producing only GIN. While we do have a logo for our distillery, we are still in search of a winning design for our Gin bottle. We are looking for something modern yet classy. Let your creativity run wild. Play around with colours, think out of the box….The winning designer will be challenged to create the coolest labels for the different flavours of Gin we will be producing in the near future. The label will maintain the same design elements throughout the design, but will also be able to differentiate each variety clearly. So for e.g. A flowery Vantoor Gin can have a pink label with a different description and a spicy Vantoor gin can have another colour with another description and so on. If the design really appeals to us, we might also invite the designer to do our website for us!

In a nutshell: It is a 500 ml bottle, (Please check the attachment so you get an idea as to what kind of bottle to imagine while making the labels). The bottle is going to have a light coloured wooden lid/cork to it. As of now we have a transparent seal to complete the sealing process once the bottling is done. The idea is that we will have two labels. One in the front and one behind. The size of the labels are as follows:

Front label: 102 x 76 mm the front label. (TO BE USED HORIZONTALLY). The details that we need on the front label are in a separate attachment.

Back label: The size for the label at the back of the bottle is: 76 x 51 mm (TO BE USED VERTICALLY) The information that needs to come on the label behind is also in the same document which is attached separately. The label behind will also have batch no. & date (Please refer to attachment to understand what I mean by batch no. date, distiller’s signature etc.) I have attached a picture of an already existing brand which has its batch number and distillers signature etc on it….so you can understand what I exactly mean by that. Please do not copy their design, this is purely to give you an idea as to what I mean by batch number and so on. The address of the distillery can be put horizontally, vertically, on the side along one border, or however you find appropriate. This is the address:
Klaverhoekstraat 41,
6318 KT, Hengelo.
The Netherlands.
www.vantoor.nl

Logo’s no drinking when pregnant, No driving and drinking, No drinking under the age of 18 need to be present on the label behind. Alternately, we can also have www.calm-sipping.com instead of the under 18 no alcohol sign, most alcohol bottles these days have it. Please let me know what else you would need from me for this. So be creative and do your best!

Thanks and regards, Marisol Vendekampa.

Target Market(s)

Largely males and females between 25-55 , the audience could even be slightly older.

Colors

Designer to choose colors to be used in the design.

Requirements
Must have
• 1) The labels need to be modern, yet classy, elite..
• 2) We need to specify the fact that we are a craft distillery and the gin is HANDMADE, using only the highest quality ingredients.
• 3) We at Vantoor live, breathe, dream, talk about our dream which is our distillery and its product. The label needs to bring home this point and should clearly specify and mention that it is produced and bottled in The Netherlands. Or handmade and bottled with love and passion in The Netherlands or something to that effect if it matches with the rest of the design.
• 4) The colours you chose must match in some way or the other with the colours used for the logo design.
Nice to have
• Would be nice to have colours and look bold, although not completely necessary.
Should not have
• What I definitely do not want is something too whacky like a skull or some kind of vague work of art. For the rest, I leave it upto you….!

```html
<!DOCTYPE html>
<html lang="en">
<head>
<meta charset="utf-8">
<title>Vantoor Gin – Front Label</title>
<link href="https://fonts.googleapis.com/css2?family=Rye&family=Old+Standard+TT:wght@400;700&family=Montserrat:wght@700&family=Kaushan+Script&display=swap" rel="stylesheet">
<style>
  :root {
    --page-bg: #1b1b1b;
    --label-light: #f7f7f7;
    --label-shade: #e6e6e6;
    --ink: #1e1e1e;
    --ink-soft: #8a8a8a;
    --rule: #9a9a9a;
    --brand-red: #e53a2c;
    --brand-orange: #f07a3c;
    --panel-grey: #cfcfcf;
    --bar-black: #111111;
    --white: #ffffff;
  }
  * { margin: 0; padding: 0; box-sizing: border-box; }
  html, body {
    width: 769px; height: 1200px; overflow: hidden;
    background: var(--page-bg);
  }
  .canvas { position: relative; width: 769px; height: 1200px; }

  .front-label {
    position: absolute; left: 44px; top: 346px;
    width: 680px; height: 507px;
    background: radial-gradient(ellipse at 50% 40%, var(--label-light), var(--label-shade));
    color: var(--ink);
  }
  .frame { position: absolute; inset: 0; width: 100%; height: 100%; }

  .corner-ornament {
    position: absolute; width: 66px; height: 66px;
    background: radial-gradient(circle, #5a5a5a 0%, #9b9b9b 60%, transparent 72%);
    opacity: .55;
  }
  .corner-ornament.top-left { left: 14px; top: 14px; }
  .corner-ornament.top-right { right: 14px; top: 14px; }
  .corner-ornament.bottom-left { left: 14px; bottom: 14px; }
  .corner-ornament.bottom-right { right: 14px; bottom: 14px; }

  .brand-name {
    position: absolute; left: 0; right: 0; top: 52px;
    text-align: center;
    font-family: "Rye", serif; font-size: 58px; line-height: 1;
    color: var(--brand-red);
  }
  .distillery {
    position: absolute; left: 0; right: 0; top: 127px;
    text-align: center;
    font-family: "Montserrat", sans-serif; font-weight: 700;
    font-size: 19px; letter-spacing: 7px; color: var(--ink);
  }
  .tagline {
    position: absolute; top: 122px;
    font-family: "Kaushan Script", cursive; font-size: 21px;
    color: var(--ink-soft);
  }
  .tagline.left { left: 86px; }
  .tagline.right { right: 82px; }

  .gin-name {
    position: absolute; left: 0; right: 0; top: 186px;
    text-align: center;
    font-family: "Rye", serif; font-size: 68px; line-height: 1;
    color: var(--ink);
    text-shadow: 3px 3px 0 #b8b8b8;
  }
  .gin-style {
    position: absolute; left: 0; right: 0; top: 290px;
    text-align: center;
    font-family: "Rye", serif; font-size: 36px; line-height: 1;
    color: var(--ink);
    text-shadow: 2px 2px 0 #bdbdbd;
  }

  .origin-seal {
    position: absolute; left: 78px; top: 340px;
    width: 132px; height: 132px; border-radius: 50%;
    background: var(--brand-red);
    box-shadow: 0 0 0 6px #d4d4d4;
    z-index: 2;
  }

  .facts-panel {
    position: absolute; left: 189px; top: 356px;
    width: 410px; height: 112px;
    background: var(--panel-grey); border-radius: 10px;
  }
  .facts-panel .claim {
    position: absolute; left: 34px; top: 6px;
    font-family: "Old Standard TT", serif; font-size: 22px; letter-spacing: .5px;
  }
  .facts-panel .claim-bar {
    position: absolute; left: 33px; top: 39px; width: 367px; height: 29px;
    background: var(--bar-black); color: var(--white);
    font-family: "Old Standard TT", serif; font-size: 20px; letter-spacing: 1px;
    text-align: center; line-height: 29px;
  }
  .spec-row {
    position: absolute; left: 34px; right: 10px; top: 76px;
    display: flex; align-items: flex-start;
    font-family: "Old Standard TT", serif;
  }
  .spec { text-align: center; line-height: 1; }
  .spec .value { font-size: 20px; display: block; }
  .spec .unit { font-size: 7px; letter-spacing: .5px; display: block; margin-top: 1px; }
  .spec-divider { width: 1px; height: 24px; background: var(--ink); margin: 0 22px; }
</style>
</head>
<body>
<main class="canvas">
  <section class="front-label" aria-label="Vantoor Gin front label">
    <svg class="frame" viewBox="0 0 680 507" aria-hidden="true">
      <rect x="10" y="10" width="660" height="487" fill="none" stroke="#8a8a8a" stroke-width="1"/>
      <rect x="16" y="16" width="648" height="475" fill="none" stroke="#8a8a8a" stroke-width="2"/>
      <line x1="72" y1="170" x2="607" y2="170" stroke="#9a9a9a" stroke-width="2"/>
      <circle cx="80" cy="170" r="4" fill="#9a9a9a"/>
      <circle cx="599" cy="170" r="4" fill="#9a9a9a"/>
      <circle cx="340" cy="170" r="3" fill="#9a9a9a"/>
      <line x1="72" y1="273" x2="607" y2="273" stroke="#9a9a9a" stroke-width="2"/>
      <circle cx="80" cy="273" r="4" fill="#9a9a9a"/>
      <circle cx="599" cy="273" r="4" fill="#9a9a9a"/>
      <circle cx="340" cy="273" r="3" fill="#9a9a9a"/>
    </svg>

    <div class="corner-ornament top-left" role="img" aria-label="Flourish ornament"></div>
    <div class="corner-ornament top-right" role="img" aria-label="Flourish ornament"></div>
    <div class="corner-ornament bottom-left" role="img" aria-label="Flourish ornament"></div>
    <div class="corner-ornament bottom-right" role="img" aria-label="Flourish ornament"></div>

    <div class="brand-name">VANTOOR</div>
    <div class="distillery">DISTILLERY</div>
    <div class="tagline left">Handcrafted</div>
    <div class="tagline right">Small batch</div>

    <h1 class="gin-name">VANTOOR GIN</h1>
    <h2 class="gin-style">PREMIUM LONDON DRY</h2>

    <div class="origin-seal" role="img" aria-label="Seal with map of The Netherlands: Product of The Netherlands"></div>

    <div class="facts-panel">
      <p class="claim">100% NATURAL BOTANICALS</p>
      <p class="claim-bar">NO ARTIFICIAL FLAVOURING</p>
      <div class="spec-row">
        <div class="spec"><span class="value">43%</span><span class="unit">ALC/VOL</span></div>
        <div class="spec-divider"></div>
        <div class="spec"><span class="value">L100/2018</span><span class="unit">BATCH NO.</span></div>
        <div class="spec-divider"></div>
        <div class="spec"><span class="value">750</span><span class="unit">ML</span></div>
        <div class="spec-divider"></div>
        <div class="spec"><span class="value">50</span><span class="unit">CL</span></div>
      </div>
    </div>
  </section>
</main>
</body>
</html>
```